Banner Ad Design Project

We need a Banner Ad design for an online company called Marlow's Signatures. We sell autographed sports & entertainment memorabilia along with licensed sports collectibles. Our product line includes, autographed sports jerseys, autographed photographs, and sports equipment such as hockey pucks, baseballs, footballs, and football helmets,plus many more We also have a large selection sports display cases.

In addition to our products, we offer a comprehensive fund raising program utilizing our products, also we offer custom sports framing.

We are looking for a Banner Ad that touches on some of our products and services. We would like it to have our company logo and some product images included.

Target Market(s)

Male. 25-30 yrs approx income of 50,000-65,000

Industry/Entity Type

Entertainment

Requirements
Must have
• Company logo.
Product images

```html
<!DOCTYPE html>
<html lang="en">
<head>
<meta charset="utf-8">
<title>Marlow's Signatures – Banner Ad</title>
<link rel="stylesheet" href="https://fonts.googleapis.com/css2?family=Arimo:wght@400;700&display=swap">
<style>
  :root {
    --navy: #1b2a7e;
    --ink-blue: #1e2c8c;
    --red: #d3262c;
    --paper: #f4f5f5;
    --paper-edge: #d4d8d8;
    --art-dark: #3a2a22;
    --art-warm: #b8552a;
    --art-light: #e9e6e1;
  }
  * { margin: 0; padding: 0; box-sizing: border-box; }
  html, body {
    width: 1200px;
    height: 900px;
    overflow: hidden;
  }
  body {
    background: #ffffff;
    font-family: "Arimo", Arial, sans-serif;
  }
  .banner {
    position: absolute;
    left: 70px;
    top: 0;
    width: 1060px;
    height: 900px;
    background: radial-gradient(ellipse at 50% 55%, #ffffff 0%, var(--paper) 45%, var(--paper-edge) 100%);
    box-shadow: 0 0 30px rgba(0, 0, 0, 0.4);
  }
  .product-art {
    position: absolute;
    left: 200px;
    top: 12px;
    width: 700px;
    height: 330px;
    border-radius: 40px;
    background: radial-gradient(ellipse at 50% 45%, var(--art-warm) 0%, var(--art-dark) 55%, var(--art-light) 100%);
  }
  .brand-name {
    position: absolute;
    left: 0;
    top: 338px;
    width: 100%;
    font-weight: 700;
    color: var(--navy);
    text-align: center;
  }
  .brand-name__main {
    display: block;
    font-size: 140px;
    line-height: 150px;
    letter-spacing: 4px;
  }
  .brand-name__sub {
    display: block;
    font-size: 92px;
    line-height: 110px;
    padding-left: 220px;
  }
  .brand-mark {
    position: absolute;
    left: 330px;
    top: 198px;
    width: 30px;
    height: 30px;
    background: var(--red);
  }
  .tagline {
    position: absolute;
    left: 0;
    top: 612px;
    width: 100%;
    text-align: center;
    font-weight: 400;
    font-size: 40px;
    color: var(--ink-blue);
  }
  .product-line {
    position: absolute;
    left: 210px;
    top: 676px;
    width: 640px;
    text-align: center;
    font-size: 19px;
    line-height: 1.3;
    color: var(--ink-blue);
  }
  .web-address {
    position: absolute;
    left: 0;
    top: 762px;
    width: 100%;
    text-align: center;
    font-size: 32px;
    letter-spacing: 8px;
    color: var(--ink-blue);
  }
</style>
</head>
<body>
  <main class="banner">
    <div class="product-art" role="img" aria-label="Sports balls (baseball, basketball, football, soccer ball) behind a football scoreboard"></div>
    <h1 class="brand-name">
      <span class="brand-name__main">MARLOW'S</span>
      <span class="brand-mark" aria-hidden="true"></span>
      <span class="brand-name__sub">Signatures</span>
    </h1>
    <p class="tagline">Sports &amp; Entertainment Memorabilia</p>
    <p class="product-line">Our product line includes, autographed sports jerseys, autographed photographs, and sports equipment such as hockey pucks, baseballs, footballs, football helmets, and large selection sports display cases.</p>
    <p class="web-address">MARLOWSSIGNATURES.COM</p>
  </main>
</body>
</html>
```